sommelier *

Sommelier Wine Hospitality Corvanne Star experience I'm working as a sommelier in a Corvanne Star restaurant. I try to reach People who are interested in invest in wine and wine loovers! In terms of color I would like to have a nice color based on a nice bordeaux red (as an advice). By the way i forgot to write my phone number and my email address. 439812604731 kdervin7@postiko.com I hope this info is enough so far.

```html
<!DOCTYPE html>
<html lang="en">
<head>
<meta charset="utf-8">
<title>Kasimir Dervin – Sommelier Business Card</title>
<link href="https://fonts.googleapis.com/css2?family=Marcellus&family=Jost:wght@200;300&display=swap" rel="stylesheet">
<style>
  :root {
    --backdrop: #c8dae9;
    --card-black: #050505;
    --wine-red: #d4173b;
    --wine-deep: #7a0d1e;
    --muted-grey: #3e3e3e;
    --phone-grey: #4d4d4d;
    --glass-grey: #3a3a3e;
    --label-white: #d9d9d9;
    --cork-tan: #b08a5c;
  }
  * { box-sizing: border-box; margin: 0; padding: 0; }
  html, body { width: 1200px; height: 1200px; overflow: hidden; }
  body {
    background: var(--backdrop);
    display: flex;
    flex-direction: column;
    align-items: center;
    justify-content: center;
    gap: 40px;
  }
  .card {
    position: relative;
    width: 840px;
    height: 480px;
    background: var(--card-black);
    border-radius: 6px;
    overflow: hidden;
    box-shadow: 0 10px 30px rgba(40, 60, 90, 0.25);
  }

  /* Back side */
  .card-back .photo-glass {
    position: absolute;
    top: 0;
    right: 0;
    width: 660px;
    height: 100%;
    background:
      radial-gradient(ellipse 38% 22% at 78% 52%, rgba(212, 23, 59, 0.75) 0%, rgba(122, 13, 30, 0.45) 45%, transparent 100%),
      radial-gradient(ellipse 22% 16% at 18% 78%, rgba(212, 23, 59, 0.7) 0%, rgba(122, 13, 30, 0.35) 50%, transparent 100%),
      radial-gradient(ellipse 55% 34% at 50% 62%, rgba(90, 90, 96, 0.55) 0%, rgba(40, 40, 44, 0.4) 50%, transparent 100%),
      var(--card-black);
  }
  .card-back .venue {
    position: absolute;
    top: 40px;
    left: 150px;
    transform-origin: top left;
    transform: rotate(90deg);
    font-family: "Marcellus", serif;
    font-size: 52px;
    line-height: 1.05;
    color: var(--wine-red);
    white-space: nowrap;
  }

  /* Front side */
  .card-front .photo-bottle {
    position: absolute;
    top: 0;
    right: 0;
    width: 400px;
    height: 100%;
    background:
      radial-gradient(ellipse 28% 11% at 52% 30%, rgba(217, 217, 217, 0.85) 0%, rgba(160, 160, 160, 0.5) 55%, transparent 100%),
      radial-gradient(ellipse 16% 22% at 58% 76%, rgba(176, 138, 92, 0.8) 0%, rgba(120, 90, 55, 0.4) 55%, transparent 100%),
      radial-gradient(ellipse 18% 8% at 22% 88%, rgba(176, 138, 92, 0.55) 0%, transparent 100%),
      radial-gradient(ellipse 36% 60% at 50% 50%, rgba(58, 58, 62, 0.7) 0%, rgba(25, 25, 27, 0.5) 55%, transparent 100%),
      radial-gradient(ellipse 16% 30% at 12% 30%, rgba(122, 13, 30, 0.5) 0%, transparent 100%),
      var(--card-black);
  }
  .card-front .identity {
    position: absolute;
    left: 80px;
    top: 180px;
  }
  .card-front .name {
    font-family: "Marcellus", serif;
    font-weight: 400;
    font-size: 62px;
    line-height: 1;
    color: var(--wine-red);
    white-space: nowrap;
  }
  .card-front .role {
    font-family: "Marcellus", serif;
    font-size: 40px;
    line-height: 1.1;
    color: var(--muted-grey);
    margin-top: 4px;
    margin-left: 14px;
  }
  .card-front .contact {
    position: absolute;
    left: 110px;
    bottom: 56px;
    display: flex;
    flex-direction: column;
    gap: 10px;
  }
  .card-front .contact-row {
    display: flex;
    align-items: center;
    gap: 14px;
  }
  .card-front .contact-icon { width: 40px; height: 40px; flex: none; }
  .card-front .contact-text {
    font-family: "Jost", sans-serif;
    font-weight: 200;
    font-size: 36px;
    color: var(--phone-grey);
    letter-spacing: 0.5px;
    white-space: nowrap;
  }
  .card-front .contact-text.email { font-size: 26px; font-weight: 300; }
</style>
</head>
<body>
  <section class="card card-back" aria-label="Card back">
    <div class="photo-glass" role="img" aria-label="Tilted wine glass with red wine splashing on a black background"></div>
    <p class="venue">Corvanne Star<br>Restaurant</p>
  </section>

  <section class="card card-front" aria-label="Card front">
    <div class="photo-bottle" role="img" aria-label="Dark wine bottle with blank label, wine glass, cork and wooden corkscrew"></div>
    <div class="identity">
      <h1 class="name">Kasimir Dervin</h1>
      <p class="role">sommelier</p>
    </div>
    <div class="contact">
      <div class="contact-row">
        <svg class="contact-icon" viewBox="0 0 46 46" aria-hidden="true">
          <circle cx="23" cy="23" r="23" fill="var(--wine-red)"/>
          <path d="M15 13c1-1 2.5-1 3.3 0l2.6 3.4c.6.8.5 1.9-.2 2.6l-1.6 1.5c1.2 2.6 3.3 4.7 5.9 5.9l1.5-1.6c.7-.7 1.8-.8 2.6-.2l3.4 2.6c1 .8 1 2.3 0 3.3l-1.6 1.6c-1.2 1.2-3 1.6-4.6 1-6.3-2.3-11.3-7.3-13.6-13.6-.6-1.6-.2-3.4 1-4.6z" fill="#0a0a0a"/>
        </svg>
        <span class="contact-text phone">+439812604731</span>
      </div>
      <div class="contact-row">
        <svg class="contact-icon" viewBox="0 0 46 46" aria-hidden="true">
          <circle cx="23" cy="23" r="23" fill="var(--wine-red)"/>
          <rect x="12" y="15" width="22" height="16" rx="2" fill="#0a0a0a"/>
          <path d="M13 17l10 7 10-7" fill="none" stroke="var(--wine-red)" stroke-width="2"/>
        </svg>
        <span class="contact-text email">kdervin7@postiko.com</span>
      </div>
    </div>
  </section>
</body>
</html>
```